We need to have 2 different retractable banners designed that will be used at a variety of events. We plan to have the banners printed through printbriskly.example. According to their site, specs are as follows: Retractable banners are digitally printed on 12oz double-sided smooth vinyl. While the area on the retractable banners is 33 x 78, the customer will want to provide a file that has an area of 35 x 82 to account for bleed, with 3" of that vertical bleed at the bottom of the design. Recommneded DPI is 150. Upload capacity for retractable banners is 100MP.

Banner #1: Cascadia Labor Alliance logo at top; then the following text placed lower on the banner: Providing leadership that promotes and advances Oregon's workforce system. At the bottom of banner: cascadialabor alliance.example

Banner #2: Cascadia Labor Alliance logo at top; then the following text placed lower on the banner: Oregon's workforce system ensures all Oregonians possess the talent needed for communities to thrive and prosper. At the bottom of banner: cascadialaboralliance.example

Color scheme: complimentary colors of the Cascadia Labor Alliance logo.
Images: images representative of Oregon (for example: map of Oregon, Douglas fir trees, coastal range, etc.

I've attached a couple of previous banners created as a reference.

```html
<!DOCTYPE html>
<html lang="en">
<head>
<meta charset="utf-8">
<title>Cascadia Labor Alliance – Retractable Banner Concepts</title>
<link rel="stylesheet" href="https://fonts.googleapis.com/css2?family=Montserrat:wght@400;500;600;800;900&family=Roboto+Condensed:wght@700&display=swap">
<style>
  :root {
    --stage: #8ea5b0;
    --stage-light: #a9bcc5;
    --navy: #1c2765;
    --navy-deep: #141c50;
    --navy-light: #2c3f8f;
    --magenta: #9b1c5c;
    --periwinkle: #6c85e0;
    --gold: #e9c45c;
    --white: #ffffff;
    --label: #ffffff;
    --label-faint: rgba(255, 255, 255, 0.28);
  }
  * { margin: 0; padding: 0; box-sizing: border-box; }
  html, body { width: 1200px; height: 2224px; overflow: hidden; }
  body {
    position: relative;
    background: linear-gradient(180deg, var(--stage) 0%, var(--stage-light) 50%, var(--stage) 100%);
    font-family: "Montserrat", sans-serif;
  }
  .sample-label {
    position: absolute;
    width: 404px;
    text-align: center;
    color: var(--label);
    font: 500 19px "Montserrat", sans-serif;
    letter-spacing: 0.5px;
  }
  .row-label {
    position: absolute;
    left: 104px;
    transform: translate(-50%, -50%) rotate(-90deg);
    color: var(--label-faint);
    font: 900 66px "Montserrat", sans-serif;
    letter-spacing: 2px;
    white-space: nowrap;
  }
  .banner {
    position: absolute;
    width: 404px;
    height: 906px;
    display: block;
    box-shadow: 0 6px 18px rgba(0, 0, 0, 0.18);
  }
  .col-a { left: 182px; }
  .col-b { left: 689px; }
  .row-1 { top: 104px; }
  .row-2 { top: 1214px; }
  .brand-name { font: 600 19px "Montserrat", sans-serif; fill: var(--navy); letter-spacing: 1px; }
  .headline { font: 800 50px "Montserrat", sans-serif; }
  .subline { font: 500 23px "Montserrat", sans-serif; fill: var(--white); }
  .accent-big { font: 800 40px "Montserrat", sans-serif; fill: var(--gold); }
  .accent-small { font: 700 27px "Montserrat", sans-serif; fill: var(--gold); letter-spacing: 1px; }
  .body-copy { font: 500 21px "Montserrat", sans-serif; fill: var(--white); }
  .url-text { font: 700 20px "Roboto Condensed", sans-serif; fill: var(--navy-deep); }
</style>
</head>
<body>

<div class="sample-label" style="left:182px; top:46px;">SAMPLE 1</div>
<div class="sample-label" style="left:689px; top:46px;">SAMPLE 2</div>
<div class="row-label" style="top:540px;">BANNER 1</div>

<div class="sample-label" style="left:182px; top:1153px;">SAMPLE 1</div>
<div class="sample-label" style="left:689px; top:1153px;">SAMPLE 2</div>
<div class="row-label" style="top:1735px;">BANNER 2</div>

<svg width="0" height="0" style="position:absolute">
  <defs>
    <linearGradient id="navy-field" x1="0" y1="0" x2="0.4" y2="1">
      <stop offset="0" stop-color="#26367f"/>
      <stop offset="0.5" stop-color="#1c2765"/>
      <stop offset="1" stop-color="#141c50"/>
    </linearGradient>
    <linearGradient id="silver-type" x1="0" y1="0" x2="0" y2="1">
      <stop offset="0" stop-color="#ffffff"/>
      <stop offset="0.55" stop-color="#e6e8ee"/>
      <stop offset="1" stop-color="#b9bdc8"/>
    </linearGradient>
    <linearGradient id="pill" x1="0" y1="0" x2="0" y2="1">
      <stop offset="0" stop-color="#ffffff"/>
      <stop offset="1" stop-color="#dcdfe6"/>
    </linearGradient>
    <linearGradient id="idea-photo" x1="0" y1="0" x2="0" y2="1">
      <stop offset="0" stop-color="#4f5964"/>
      <stop offset="0.5" stop-color="#3b434d"/>
      <stop offset="1" stop-color="#2a3038"/>
    </linearGradient>
    <radialGradient id="idea-glow" cx="0.4" cy="0.35" r="0.4">
      <stop offset="0" stop-color="#f6d58a"/>
      <stop offset="1" stop-color="#f6d58a" stop-opacity="0"/>
    </radialGradient>
    <linearGradient id="summit-photo" x1="0" y1="0" x2="0" y2="1">
      <stop offset="0" stop-color="#fbf6ee"/>
      <stop offset="0.3" stop-color="#f1d7a4"/>
      <stop offset="0.6" stop-color="#dca460"/>
      <stop offset="1" stop-color="#6b4428"/>
    </linearGradient>
    <linearGradient id="hands-photo" x1="0" y1="0" x2="1" y2="1">
      <stop offset="0" stop-color="#4d6a2e"/>
      <stop offset="0.5" stop-color="#c99a7e"/>
      <stop offset="1" stop-color="#56712f"/>
    </linearGradient>
    <linearGradient id="team-photo" x1="0" y1="0" x2="0" y2="1">
      <stop offset="0" stop-color="#f1f1ee"/>
      <stop offset="0.45" stop-color="#e3ddd6"/>
      <stop offset="1" stop-color="#c9c7cc"/>
    </linearGradient>
    <linearGradient id="silver-arc" x1="0" y1="0" x2="1" y2="1">
      <stop offset="0" stop-color="#ffffff"/>
      <stop offset="1" stop-color="#a9adb6"/>
    </linearGradient>
  </defs>
</svg>

<!-- Banner 1 · Sample 1 -->
<svg class="banner col-a row-1" viewBox="0 0 468 1050" aria-label="Banner 1, sample 1">
  <rect width="468" height="1050" fill="var(--white)"/>
  <g role="img" aria-label="Photo: hand touching a glowing light bulb among sketched bulbs">
    <rect y="150" width="468" height="500" fill="url(#idea-photo)"/>
    <rect y="150" width="468" height="500" fill="url(#idea-glow)"/>
  </g>
  <path d="M0 0 H468 V158 C420 200 350 206 260 200 C160 194 70 196 0 212 Z" fill="var(--white)"/>
  <path d="M0 212 C70 196 160 194 260 200 C350 206 420 200 468 158 V180 C420 225 350 240 260 234 C160 226 70 222 0 232 Z" fill="var(--periwinkle)"/>
  <rect x="179" y="28" width="110" height="104" fill="var(--magenta)"/>
  <text class="brand-name" x="234" y="157" text-anchor="middle">CASCADIA LABOR</text>
  <text class="brand-name" x="234" y="179" text-anchor="middle">ALLIANCE</text>
  <path d="M0 615 C90 560 180 555 260 575 C350 597 420 598 468 580 V1050 H0 Z" fill="var(--magenta)"/>
  <path d="M0 634 C90 576 180 571 260 590 C350 611 420 611 468 596" fill="none" stroke="var(--white)" stroke-width="5"/>
  <path d="M0 640 C90 582 180 577 260 596 C350 617 420 617 468 602 V1050 H0 Z" fill="url(#navy-field)"/>
  <text class="headline" x="234" y="698" text-anchor="middle" fill="url(#silver-type)" textLength="335" lengthAdjust="spacingAndGlyphs">PROVIDING</text>
  <text class="headline" x="234" y="749" text-anchor="middle" fill="url(#silver-type)" textLength="370" lengthAdjust="spacingAndGlyphs">LEADERSHIP</text>
  <text class="subline" x="234" y="793" text-anchor="middle">That Promotes and</text>
  <text class="subline" x="234" y="820" text-anchor="middle">Advances</text>
  <text class="accent-big" x="234" y="874" text-anchor="middle" textLength="244" lengthAdjust="spacingAndGlyphs">OREGON'S</text>
  <text class="accent-small" x="234" y="906" text-anchor="middle" textLength="340" lengthAdjust="spacingAndGlyphs">WORKFORCE SYSTEM.</text>
  <rect x="33" y="940" width="403" height="42" rx="8" fill="url(#pill)"/>
  <text class="url-text" x="234" y="968" text-anchor="middle" textLength="370" lengthAdjust="spacingAndGlyphs">CASCADIALABORALLIANCE.EXAMPLE</text>
</svg>

<!-- Banner 1 · Sample 2 -->
<svg class="banner col-b row-1" viewBox="0 0 468 1050" aria-label="Banner 1, sample 2">
  <g role="img" aria-label="Photo: three people celebrating on a mountain summit at sunset">
    <rect width="468" height="650" fill="url(#summit-photo)"/>
  </g>
  <rect x="179" y="28" width="110" height="104" fill="var(--magenta)"/>
  <text class="brand-name" x="234" y="157" text-anchor="middle">CASCADIA LABOR</text>
  <text class="brand-name" x="234" y="179" text-anchor="middle">ALLIANCE</text>
  <path d="M0 615 C90 560 180 555 260 575 C350 597 420 598 468 580 V1050 H0 Z" fill="var(--magenta)"/>
  <path d="M0 634 C90 576 180 571 260 590 C350 611 420 611 468 596" fill="none" stroke="var(--white)" stroke-width="5"/>
  <path d="M0 640 C90 582 180 577 260 596 C350 617 420 617 468 602 V1050 H0 Z" fill="url(#navy-field)"/>
  <text class="headline" x="234" y="698" text-anchor="middle" fill="url(#silver-type)" textLength="335" lengthAdjust="spacingAndGlyphs">PROVIDING</text>
  <text class="headline" x="234" y="749" text-anchor="middle" fill="url(#silver-type)" textLength="370" lengthAdjust="spacingAndGlyphs">LEADERSHIP</text>
  <text class="subline" x="234" y="793" text-anchor="middle">That Promotes and</text>
  <text class="subline" x="234" y="820" text-anchor="middle">Advances</text>
  <text class="accent-big" x="234" y="874" text-anchor="middle" textLength="244" lengthAdjust="spacingAndGlyphs">OREGON'S</text>
  <text class="accent-small" x="234" y="906" text-anchor="middle" textLength="340" lengthAdjust="spacingAndGlyphs">WORKFORCE SYSTEM.</text>
  <rect x="33" y="940" width="403" height="42" rx="8" fill="url(#pill)"/>
  <text class="url-text" x="234" y="968" text-anchor="middle" textLength="370" lengthAdjust="spacingAndGlyphs">CASCADIALABORALLIANCE.EXAMPLE</text>
</svg>

<!-- Banner 2 · Sample 1 -->
<svg class="banner col-a row-2" viewBox="0 0 468 1050" aria-label="Banner 2, sample 1">
  <rect width="468" height="1050" fill="var(--white)"/>
  <rect x="179" y="28" width="110" height="104" fill="var(--magenta)"/>
  <text class="brand-name" x="234" y="157" text-anchor="middle">CASCADIA LABOR</text>
  <text class="brand-name" x="234" y="179" text-anchor="middle">ALLIANCE</text>
  <rect y="560" width="468" height="490" fill="url(#navy-field)"/>
  <g role="img" aria-label="Photo: many hands clasping wrists in a circle over grass">
    <path d="M0 275 C35 222 105 201 200 201 H468 V520 C440 585 370 614 280 614 H0 Z" fill="url(#hands-photo)"/>
  </g>
  <path d="M0 290 C25 232 95 206 190 203" fill="none" stroke="url(#silver-arc)" stroke-width="8"/>
  <path d="M468 505 C445 570 385 608 300 614" fill="none" stroke="url(#silver-arc)" stroke-width="8"/>
  <rect y="614" width="468" height="436" fill="url(#navy-field)"/>
  <text class="headline" x="234" y="693" text-anchor="middle" fill="url(#silver-type)" textLength="310" lengthAdjust="spacingAndGlyphs">OREGON'S</text>
  <text class="headline" x="234" y="748" text-anchor="middle" fill="url(#silver-type)" textLength="385" lengthAdjust="spacingAndGlyphs">WORKFORCE</text>
  <text class="headline" x="234" y="803" text-anchor="middle" fill="url(#silver-type)" textLength="235" lengthAdjust="spacingAndGlyphs">SYSTEM</text>
  <text class="body-copy" x="234" y="844" text-anchor="middle">ensures all Oregonians possess</text>
  <text class="body-copy" x="234" y="871" text-anchor="middle">the talent needed for</text>
  <text class="body-copy" x="234" y="897" text-anchor="middle">communities to thrive and prosper.</text>
  <rect x="33" y="939" width="403" height="42" rx="8" fill="url(#pill)"/>
  <text class="url-text" x="234" y="967" text-anchor="middle" textLength="370" lengthAdjust="spacingAndGlyphs">CASCADIALABORALLIANCE.EXAMPLE</text>
</svg>

<!-- Banner 2 · Sample 2 -->
<svg class="banner col-b row-2" viewBox="0 0 468 1050" aria-label="Banner 2, sample 2">
  <g role="img" aria-label="Photo: smiling team of diverse coworkers standing in a bright office">
    <rect width="468" height="640" fill="url(#team-photo)"/>
  </g>
  <rect x="179" y="28" width="110" height="104" fill="var(--magenta)"/>
  <text class="brand-name" x="234" y="157" text-anchor="middle">CASCADIA LABOR</text>
  <text class="brand-name" x="234" y="179" text-anchor="middle">ALLIANCE</text>
  <path d="M0 500 Q234 700 468 500 V1050 H0 Z" fill="var(--magenta)"/>
  <path d="M0 524 Q234 716 468 524" fill="none" stroke="var(--white)" stroke-width="5"/>
  <path d="M0 530 Q234 722 468 530 V1050 H0 Z" fill="url(#navy-field)"/>
  <text class="headline" x="234" y="693" text-anchor="middle" fill="url(#silver-type)" textLength="310" lengthAdjust="spacingAndGlyphs">OREGON'S</text>
  <text class="headline" x="234" y="748" text-anchor="middle" fill="url(#silver-type)" textLength="385" lengthAdjust="spacingAndGlyphs">WORKFORCE</text>
  <text class="headline" x="234" y="803" text-anchor="middle" fill="url(#silver-type)" textLength="235" lengthAdjust="spacingAndGlyphs">SYSTEM</text>
  <text class="body-copy" x="234" y="844" text-anchor="middle">ensures all Oregonians possess</text>
  <text class="body-copy" x="234" y="871" text-anchor="middle">the talent needed for</text>
  <text class="body-copy" x="234" y="897" text-anchor="middle">communities to thrive and prosper.</text>
  <rect x="33" y="939" width="403" height="42" rx="8" fill="url(#pill)"/>
  <text class="url-text" x="234" y="967" text-anchor="middle" textLength="370" lengthAdjust="spacingAndGlyphs">CASCADIALABORALLIANCE.EXAMPLE</text>
</svg>

</body>
</html>
```